Dating & Relationship Coach Needs a Business Card Designed

I need a new business card designed that's targeted at women aged 30-45 who want to find their Soul-Mate. I coach clients privately, run group programs and workshops called Kindred-Spark Method, How to Meet The Partner Who Lights You Up (tag line), which is also now an eCourse. My overall brand is called Walking A Bold Path (walkingaboldpath.com) where I teach women how to Create Connection With Anyone, Anywhere, Anytime (tag line). I have logos for both Walking A Bold Path and Kindred-Spark Method and use these interchangeably in videos etc, so i'm thinking a double sided card with one logo and tag line per side plus my details. My colour palette can be found at www.walkingaboldpath.com/styleguide. Id like to leave anyone who picks up my card with the feeling that anything is possible if you're brave enough.

Target Market(s)

Single women aged 30-45 who want to find their Soul-Mate.

Industry/Entity Type

Life Coaching

Contact Information for Business Card

Megan Rowe
Founder & Director | Soul-Mate Coach | Speaker
+61 412 857 219
megan@walkingaboldpath.com
www.walkingaboldpath.com
www.kindred-sparkmethod.com

Font styles to use
Other font styles liked:
• Raleway and Bellwethers

Colors
00a990
f78f20

Requirements
Must have
• Logos & Tag lines, my colour palette - see walkingaboldpath.com/styleguide, my fonts
Nice to have
• Fun, Bright, Creative

```html
<!DOCTYPE html>
<html lang="en">
<head>
<meta charset="utf-8">
<title>Walking A Bold Path – Business Card</title>
<link rel="stylesheet" href="https://fonts.googleapis.com/css2?family=Montserrat:wght@800&family=Jost:wght@400&display=swap">
<style>
  :root {
    --ink: #201c1a;
    --paper: #ffffff;
    --teal: #3a9ead;
    --orange: #e77b1e;
    --mist: #d9d9d9;
    --text: #1d1d1d;
    --rule: #8a8a8a;
  }
  * { margin: 0; padding: 0; box-sizing: border-box; }
  html, body { width: 924px; height: 1200px; overflow: hidden; background: var(--paper); }
  body { position: relative; font-family: "Jost", Arial, sans-serif; color: var(--text); }

  .side-label {
    position: absolute; left: 0; width: 924px; text-align: center;
    font-family: Arial, Helvetica, sans-serif; font-size: 33px; color: #111;
  }
  .side-label--front { top: -6px; }
  .side-label--back { top: 624px; }

  .card { position: absolute; left: 0; width: 924px; height: 520px; overflow: hidden; }
  .card--front { top: 65px; background: var(--ink); }
  .card--back { top: 680px; background: var(--paper); border: 1px solid var(--rule); }

  .brand-name {
    font-family: "Montserrat", Arial, sans-serif; font-weight: 800;
    color: var(--teal); line-height: 0.98; letter-spacing: -0.5px; text-transform: uppercase;
  }
  .card--front .brand-name { position: absolute; left: 208px; top: 133px; font-size: 58px; }
  .card--back .brand-name { position: absolute; left: 485px; top: 74px; font-size: 40px; }

  .tagline { position: absolute; text-transform: uppercase; letter-spacing: 1.4px; white-space: nowrap; }
  .card--front .tagline { left: 209px; top: 328px; font-size: 15px; color: #e6e6e6; }
  .card--back .tagline { left: 485px; top: 222px; font-size: 14.5px; color: var(--text); }

  .site-url {
    position: absolute; left: 0; width: 924px; top: 480px - 0px; text-align: center;
    font-size: 26px; color: #ffffff;
  }
  .card--front .site-url { top: 415px; }

  .contact-list { position: absolute; left: 55px; top: 294px; list-style: none; }
  .contact-item { display: flex; align-items: center; height: 41.5px; font-size: 28px; color: var(--text); }
  .contact-icon { width: 30px; height: 30px; margin-right: 18px; flex: none; }

  .accent-bands { position: absolute; left: 0; bottom: 0; width: 924px; height: 45px; }
</style>
</head>
<body>
  <div class="side-label side-label--front">Front</div>

  <section class="card card--front">
    <div class="brand-name">Walking A<br>Bold Path</div>
    <p class="tagline">Create connection with anyone, anywhere, anytime</p>
    <p class="site-url">www.walkingaboldpath.com</p>
  </section>

  <div class="side-label side-label--back">Back</div>

  <section class="card card--back">
    <div class="brand-name">Kindred-Spark<br>Method</div>
    <p class="tagline">How to meet the partner who lights you up</p>

    <ul class="contact-list">
      <li class="contact-item">
        <svg class="contact-icon" viewBox="0 0 30 30"><rect x="2" y="2" width="26" height="26" rx="4" fill="var(--teal)"/></svg>
        @meganrowe
      </li>
      <li class="contact-item">
        <svg class="contact-icon" viewBox="0 0 30 30"><rect x="2" y="2" width="26" height="26" rx="4" fill="var(--teal)"/></svg>
        @megan_rowe
      </li>
      <li class="contact-item">
        <svg class="contact-icon" viewBox="0 0 30 30"><path d="M9 4l4 5-2.5 3c1.5 3 4 5.5 7 7l3-2.5 5 4-2 4c-8 1-18-9-17-17z" fill="var(--teal)"/></svg>
        +0998 4172 615
      </li>
      <li class="contact-item">
        <svg class="contact-icon" viewBox="0 0 30 30"><rect x="2" y="7" width="26" height="17" fill="var(--teal)"/><path d="M3 8l12 9 12-9" fill="none" stroke="#fff" stroke-width="1.6"/><path d="M3 23l9-7M27 23l-9-7" stroke="#fff" stroke-width="1.4"/></svg>
        meganrowe@walkingaboldpath.com
      </li>
    </ul>

    <svg class="accent-bands" viewBox="0 0 924 45" preserveAspectRatio="none">
      <polygon points="0,0 545,0 531,45 0,45" fill="var(--orange)"/>
      <polygon points="566,0 924,0 924,45 552,45" fill="var(--teal)"/>
    </svg>
  </section>
</body>
</html>
```